Home web page re-vamp

I would like a stylish new home page design for a clients website.
I have included a sitemap to give some guidance.
The site needs to show off the design capabilitiesof the client

```html
<!DOCTYPE html>
<html lang="en">
<head>
<meta charset="utf-8">
<title>Home</title>
<link href="https://fonts.googleapis.com/css2?family=Antonio:wght@100;200;300&display=swap" rel="stylesheet">
<style>
  :root {
    --frame-black: #050505;
    --sky-deep: #3556bd;
    --sky-mid: #5a82d8;
    --sky-light: #8fb0e4;
    --haze: #d7dfe2;
    --sea: #3aa3ae;
    --sea-deep: #0f5f6c;
    --sea-dark: #0a3f4c;
    --sidebar: #d9d9d9;
    --sidebar-active: #c2c2c2;
    --divider: #8fc1d8;
    --card: rgba(236, 240, 244, 0.78);
    --ink: #111418;
  }
  * { box-sizing: border-box; margin: 0; padding: 0; }
  html, body { width: 1200px; height: 848px; overflow: hidden; background: var(--frame-black); }
  body { font-family: "Antonio", "Arial Narrow", sans-serif; color: var(--ink); }

  .page { position: relative; width: 1200px; height: 848px; overflow: hidden; }

  .frame-bar { position: absolute; left: 0; width: 1200px; background: var(--frame-black); z-index: 3; }
  .frame-bar--top { top: 0; height: 29px; }
  .frame-bar--bottom { bottom: 0; height: 22px; }

  .backdrop {
    position: absolute; left: 0; top: 29px; width: 1200px; height: 797px;
    background:
      radial-gradient(ellipse 420px 120px at 560px 470px, rgba(240,238,225,0.55), transparent 70%),
      linear-gradient(180deg,
        var(--sky-deep) 0%,
        var(--sky-mid) 14%,
        var(--sky-light) 30%,
        var(--haze) 50%,
        #a9c9cc 60%,
        var(--sea) 72%,
        var(--sea-deep) 87%,
        var(--sea-dark) 100%);
  }

  .page-title {
    position: absolute; top: 64px; left: 640px; width: 127px;
    border-top: 1.5px solid var(--ink); border-bottom: 1.5px solid var(--ink);
    text-align: center; font-weight: 200; font-size: 62px; line-height: 82px;
    letter-spacing: 1px; z-index: 2;
  }

  .side-nav {
    position: absolute; left: 0; top: 188px; width: 250px; height: 534px;
    background: var(--sidebar); z-index: 2;
  }
  .side-nav ul { list-style: none; margin-top: 84px; }
  .side-nav li {
    height: 50.5px; border-top: 1.5px solid var(--divider);
    text-align: right; padding-right: 25px;
    font-weight: 200; font-size: 29px; line-height: 49px;
  }
  .side-nav li:last-child { border-bottom: 1.5px solid var(--divider); }
  .side-nav li.is-active { background: var(--sidebar-active); }

  .info-card {
    position: absolute; width: 280px; height: 242px;
    background: var(--card); text-align: center; z-index: 2;
    font-weight: 200; font-size: 25px; line-height: 37px;
  }
  .info-card h2 { font-weight: 200; font-size: 25px; line-height: 37px; margin-bottom: 11px; }
  .info-card--why { left: 406px; top: 190px; padding-top: 24px; }
  .info-card--architects { left: 714px; top: 190px; padding-top: 24px; }
  .info-card--architects h2 { margin-bottom: 4px; }
  .info-card--fitout { left: 406px; top: 480px; padding-top: 22px; }
  .info-card--fitout h2 { margin-bottom: 8px; }
  .info-card--awards { left: 714px; top: 480px; padding-top: 22px; }
</style>
</head>
<body>
<div class="page">
  <div class="frame-bar frame-bar--top"></div>
  <div class="backdrop" role="img" aria-label="Softly blurred coastal photograph: blue sky over pale buildings and turquoise sea"></div>

  <h1 class="page-title">HOME</h1>

  <nav class="side-nav">
    <ul>
      <li class="is-active">ABOUT US</li>
      <li>SERVICES</li>
      <li>OUR CLIENTS</li>
      <li>GALLERY</li>
      <li>HEALTH &amp; SAFETY</li>
      <li>SPECIFICATION SHEETS</li>
      <li>CONTACT US</li>
    </ul>
  </nav>

  <section class="info-card info-card--why">
    <h2>WHY US ?</h2>
    <p>7 DAYS FROM QUOTATION<br>TO DELIVERY USING THE<br>LATEST TECHNOLOGY</p>
  </section>

  <section class="info-card info-card--architects">
    <h2>ARCHITECTS &amp; DESIGNERS</h2>
    <p>ADVICE ON COLOURS<br>AND MATERIALS<br>ENVIRONMENTAL FRIENDLY<br>MANUFACTURE</p>
  </section>

  <section class="info-card info-card--fitout">
    <h2>COMMERCIAL FIT OUT<br>COMPANIES</h2>
    <p>SITE SURVEYS AND<br>CONSULTATION BY OUR<br>EXPERIENCED DESIGN TEAM</p>
  </section>

  <section class="info-card info-card--awards">
    <h2>AWARDS &amp; ACCREDITATIONS</h2>
    <p>WE ARE CONTINUALLY LOOKING<br>AT HOW WE CAN IMPROVE<br>OUR SERVICES</p>
  </section>

  <div class="frame-bar frame-bar--bottom"></div>
</div>
</body>
</html>
```